Dog care service needs business card design

Our company is Pawsome Haven. We provide care for dogs while their owners are away, either through home visits or a holiday stay in the homes of carefully selected minders. Our existing website & Chatterbook cover should provide all the colour cues for our business cards - namely blues, blondes and grey. We have an existing logo (provided).

www.pawsomehaven-demo.com.au
www.facebook.com/pawsomehavenau

We wish to clearly communicate our three areas of service "dog minding, home visits, dog walking".

We would like to have the files ready for upload to Prontoprint (or similar) for immediate printing.

Target Market(s)

Dog owners who love their dogs like family

Industry/Entity Type

Business

Contact Information for Business Card

Pawsome Haven
Ph: 0491 574 318

Font styles to use
Sans Serif

Colors
33a6d7
3176b5

Requirements
Must have
• Logo
• Telephone number
• website
• "Dog minding, home visits, dog walking"
Should not have
• any additional illustrations beyond the logo.

```html
<!DOCTYPE html>
<html lang="en">
<head>
<meta charset="utf-8">
<title>Pawsome Haven – Business Card</title>
<link href="https://fonts.googleapis.com/css2?family=Open+Sans:wght@300;400;600&display=swap" rel="stylesheet">
<style>
  :root {
    --sky: #33a6d7;
    --ocean: #3176b5;
    --slate: #45566b;
    --grey-text: #5f6770;
    --paper: #ffffff;
    --paper-shade: #eef0f2;
    --backdrop: #e9e6e1;
  }
  * { margin: 0; padding: 0; box-sizing: border-box; }
  html, body {
    width: 1200px; height: 886px; overflow: hidden;
    background: var(--backdrop);
    font-family: "Open Sans", Arial, sans-serif;
  }
  .canvas { position: relative; width: 1200px; height: 886px; }

  .card {
    position: absolute;
    width: 560px; height: 342px;
    border-radius: 16px;
    overflow: hidden;
    background: linear-gradient(180deg, var(--paper) 0%, var(--paper-shade) 100%);
    box-shadow: 0 3px 0 #d5d9de, 0 6px 0 var(--ocean), 0 18px 30px rgba(0,0,0,.18);
  }
  .card-front { left: 60px; top: 70px; }
  .card-back  { left: 580px; top: 470px; }

  .card-art { position: absolute; inset: 0; width: 100%; height: 100%; }

  .brand {
    position: absolute;
    display: flex; align-items: center; gap: 12px;
    white-space: nowrap;
  }
  .brand-dot {
    flex: none;
    width: 30px; height: 30px; border-radius: 50%;
    background: var(--slate);
  }
  .brand-name {
    font-weight: 600; font-size: 32px; line-height: 1;
    color: var(--slate); letter-spacing: -0.5px;
  }
  .card-front .brand { left: 32px; top: 200px; }
  .card-back .brand  { left: 50%; top: 50%; transform: translate(-50%, -50%); }

  .person { position: absolute; right: 34px; top: 30px; text-align: right; }
  .person-name { font-weight: 300; font-size: 24px; color: var(--grey-text); }
  .person-role { font-weight: 300; font-size: 14px; color: var(--sky); margin-top: 2px; }

  .contact-list {
    position: absolute; right: 34px; top: 100px;
    list-style: none; text-align: right;
  }
  .contact-item {
    display: flex; justify-content: flex-end; align-items: center; gap: 8px;
    font-weight: 300; font-size: 12.5px; color: var(--grey-text);
    line-height: 21px;
    white-space: nowrap;
  }
  .contact-icon { width: 14px; height: 14px; flex: none; }

  .services {
    position: absolute; right: 26px; bottom: 18px;
    font-weight: 300; font-size: 17px; color: var(--paper);
    letter-spacing: .2px;
    white-space: nowrap;
  }
</style>
</head>
<body>
<main class="canvas">

  <section class="card card-front" aria-label="Business card front">
    <svg class="card-art" viewBox="0 0 560 342" preserveAspectRatio="none" aria-hidden="true">
      <defs>
        <linearGradient id="frontBand" x1="0" y1="1" x2="1" y2="0">
          <stop offset="0" stop-color="#5ab9e0"/>
          <stop offset="1" stop-color="#3176b5"/>
        </linearGradient>
      </defs>
      <path d="M30 342 Q 200 260 560 200 L560 342 Z" fill="url(#frontBand)"/>
    </svg>

    <div class="brand">
      <span class="brand-dot"></span>
      <span class="brand-name">Pawsome Haven</span>
    </div>

    <div class="person">
      <div class="person-name">Employee Name</div>
      <div class="person-role">Managing Director</div>
    </div>

    <ul class="contact-list">
      <li class="contact-item">0491 574 318
        <svg class="contact-icon" viewBox="0 0 14 14"><path d="M3 1h3l1 3-2 1c.8 1.8 2.2 3.2 4 4l1-2 3 1v3c0 .6-.4 1-1 1C6.4 13 1 7.6 1 2c0-.6.4-1 1-1z" fill="#33a6d7"/></svg>
      </li>
      <li class="contact-item">www.pawsomehaven-demo.com.au
        <svg class="contact-icon" viewBox="0 0 14 14"><circle cx="7" cy="7" r="6" fill="none" stroke="#33a6d7" stroke-width="1.4"/><ellipse cx="7" cy="7" rx="2.5" ry="6" fill="none" stroke="#33a6d7" stroke-width="1.1"/><line x1="1" y1="7" x2="13" y2="7" stroke="#33a6d7" stroke-width="1.1"/></svg>
      </li>
      <li class="contact-item">hello@pawsomehaven-demo.com.au
        <svg class="contact-icon" viewBox="0 0 14 14"><rect x="1" y="3" width="12" height="8" rx="1" fill="#33a6d7"/><path d="M1.5 3.5 7 8l5.5-4.5" fill="none" stroke="#fff" stroke-width="1"/></svg>
      </li>
      <li class="contact-item">Brookvale Heights, New South Wales, Australia 2790
        <svg class="contact-icon" viewBox="0 0 14 14"><path d="M7 1a4 4 0 0 1 4 4c0 3-4 8-4 8S3 8 3 5a4 4 0 0 1 4-4z" fill="#33a6d7"/><circle cx="7" cy="5" r="1.4" fill="#fff"/></svg>
      </li>
    </ul>

    <p class="services">Dog minding | home visits | dog walking</p>
  </section>

  <section class="card card-back" aria-label="Business card back">
    <svg class="card-art" viewBox="0 0 560 342" preserveAspectRatio="none" aria-hidden="true">
      <defs>
        <linearGradient id="backBlue" x1="0" y1="0" x2="1" y2="1">
          <stop offset="0" stop-color="#3e8fcb"/>
          <stop offset="1" stop-color="#3176b5"/>
        </linearGradient>
      </defs>
      <rect width="560" height="342" fill="url(#backBlue)"/>
      <path d="M0 70 C 180 40, 380 40, 560 10 L560 290 C 380 300, 180 310, 0 342 Z" fill="#ffffff"/>
    </svg>

    <div class="brand">
      <span class="brand-dot"></span>
      <span class="brand-name">Pawsome Haven</span>
    </div>
  </section>

</main>
</body>
</html>
```